Mt Varrowen Lamb - Online retail of "Meadow to Fork" lamb

Design and publish our website that is google tracking friendly, SEO friendly and also allows a good shop using stripe payments.
Current website is www.mvxq.com.au. All the information and data is on there. for copy past.
Also include a recipe page. not a blog, but actual recipes we can change for seasons. i.e. hearty winter meals, v summer light and playful food.
We don't want anything complex, it needs to feel trustworthy, not to busy. make it easy to click and buy.

I also want to be able to update and manage myself once running, to reduce overheads.

Also ability to link mail chip to the signup/contact information

Target Market(s)

people looking to save money and pay $15/kg, instead of supermarket chain $45/kg. People who like fresh, ethically grown produce.

Industry/Entity Type

Primary producer, Food

Coding

Coded - Design and coding required

Number of Pages Required

4 page

Font styles to use
Other font styles liked:
• Im not sure.

Requirements
Must have
• Easy functionality, trust worthy and easy use store/ordering, google tracking compatiable.
Nice to have
• Subscription, IE client signs up for a Half/Side of lamb delivered monthly for subscription fee

```html
<!DOCTYPE html>
<html lang="en">
<head>
<meta charset="utf-8">
<title>Mt Varrowen Farms – Meadow to Fork Lamb</title>
<link href="https://fonts.googleapis.com/css2?family=Archivo+Black&family=Montserrat:wght@400;500;600&family=Yellowtail&display=swap" rel="stylesheet">
<style>
:root{
  --brown:#3d3630;
  --brown-soft:#6b5d50;
  --cream:#f4f1ea;
  --butter:#ede8ae;
  --gold:#e8df86;
  --ink:#1e1a17;
  --white:#ffffff;
  --line:#b9b2a6;
}
*{box-sizing:border-box;margin:0;padding:0}
html,body{width:1200px;height:4556px;overflow:hidden}
body{position:relative;background:var(--cream);font-family:"Montserrat",sans-serif;color:var(--ink)}
.abs{position:absolute}
.display{font-family:"Archivo Black",sans-serif;text-transform:uppercase;letter-spacing:3px;color:var(--ink);line-height:1.1}
.script{font-family:"Yellowtail",cursive}
.btn{position:absolute;display:flex;align-items:center;justify-content:center;gap:10px;font-size:12px;font-weight:500;letter-spacing:.5px;text-transform:uppercase;text-decoration:none;color:var(--ink);border:1px solid var(--ink)}
.btn svg{width:14px;height:14px}
.btn--gold{background:var(--gold);border:none}
.btn--dark{background:var(--ink);color:var(--white)}
.media{position:absolute}
.site-nav{position:absolute;top:0;left:0;width:1200px;height:50px;background:var(--cream);z-index:3}
.site-nav a{position:absolute;top:18px;font-size:11px;font-weight:500;color:var(--ink);text-decoration:none}
.brand-badge{position:absolute;left:548px;top:4px;width:104px;height:78px;border-radius:50%;background:var(--cream);display:flex;align-items:center;justify-content:center;z-index:4}
.brand-badge span{font-size:10px;font-weight:600;text-align:center;line-height:1.2;width:70px}
.hero{position:absolute;top:50px;left:0;width:1200px;height:420px;background:linear-gradient(180deg,#5a4d40,#4a4035 60%,#3d342b)}
.hero .welcome{position:absolute;top:70px;width:100%;text-align:center;font-size:38px;color:var(--gold)}
.hero h1{position:absolute;top:125px;width:100%;text-align:center;font-size:52px;color:var(--white)}
.band{position:absolute;left:0;width:1200px}
.play{position:absolute;width:56px;height:56px;border-radius:50%;background:rgba(255,255,255,.25);border:2px solid rgba(255,255,255,.7);display:flex;align-items:center;justify-content:center}
.body-copy{font-size:12px;line-height:21px;color:var(--ink)}
.category{position:absolute;top:2470px;width:184px;text-align:center}
.category .disc{width:184px;height:184px;border-radius:50%;background:radial-gradient(circle,#4a423a,var(--brown) 70%)}
.category p{margin-top:28px;font-size:17px;letter-spacing:1px;line-height:1.3}
.product{position:absolute;top:3067px;width:303px}
.product .shot{width:303px;height:340px}
.product h3{margin-top:20px;font-size:12px;font-weight:500;line-height:21px}
.product .price{margin-top:10px;font-size:17px;font-weight:500}
.product .btn{position:relative;margin-top:12px;width:171px;height:40px}
.arrow-btn{position:absolute;width:56px;height:56px;border-radius:50%;background:var(--white);display:flex;align-items:center;justify-content:center;box-shadow:0 2px 6px rgba(0,0,0,.12)}
.field{position:absolute;left:661px;width:427px;border:1px solid var(--line);background:var(--cream);font-size:11px;color:#8a847a;padding:9px 16px}
.footer{position:absolute;top:4137px;left:0;width:1200px;height:419px;background:var(--brown)}
.footer nav a{position:absolute;top:186px;font-size:12px;font-weight:500;color:var(--white);text-decoration:none}
.social{position:absolute;top:244px;width:56px;height:56px;border-radius:50%;background:var(--white)}
</style>
</head>
<body>

<header class="site-nav">
  <a style="left:211px" href="#">Home</a>
  <a style="left:287px" href="#">About Us</a>
  <a style="left:381px" href="#">Our Mission</a>
  <a style="left:754px" href="#">Products</a>
  <a style="left:846px" href="#">Our Recipes</a>
  <a style="left:956px" href="#">Contact Us</a>
</header>
<div class="brand-badge"><span>Mt Varrowen Farms</span></div>

<section class="hero" role="img" aria-label="Flock of woolly sheep gathered in a dusty paddock">
  <div class="welcome script">Welcome to</div>
  <h1 class="display">Mt Varrowen Farms!</h1>
  <a class="btn btn--gold" style="left:481px;top:220px;width:219px;height:42px" href="#">Order Fresh Lamb
    <svg viewBox="0 0 14 14" fill="none" stroke="currentColor" stroke-width="1.4"><path d="M1 7h12M8 2l5 5-5 5"/></svg></a>
</section>

<div class="media" style="left:242px;top:544px;width:716px;height:174px;background:linear-gradient(90deg,#5c5148,#a39686 45%,#7b7063)" role="img" aria-label="Close-up of lambs with cartoon sheep characters peeking in"></div>
<h2 class="display abs" style="top:760px;width:1200px;text-align:center;font-size:42px">Our Story</h2>
<p class="body-copy abs" style="left:240px;top:830px;width:720px;text-align:center">Our journey began in the heart of Mount Darrowby, WA, where lush pastures and happy sheep set the scene for our vision. We dreamed of a place where the soft bleats of lambs echo through the fields, and where the love for premium lamb cuts meets the warmth of a close-knit community. Mt Varrowen Lamb Haven was born from this dream, and it's been a woolly adventure ever since!</p>
<a class="btn" style="left:481px;top:949px;width:238px;height:42px" href="#">Learn More About Us
  <svg viewBox="0 0 14 14" fill="none" stroke="currentColor" stroke-width="1.4"><path d="M1 7h12M8 2l5 5-5 5"/></svg></a>

<div class="band" style="top:1225px;height:925px;background:var(--butter)"></div>

<div class="media" style="left:48px;top:1066px;width:1102px;height:362px;background:linear-gradient(90deg,#7a6650,#8d8466 50%,#5d6148)" role="img" aria-label="Video still of sheep feeding while the farmer crouches by the fence"></div>
<div class="play" style="left:570px;top:1219px"><svg width="18" height="18" viewBox="0 0 18 18"><path d="M5 3l10 6-10 6z" fill="#fff"/></svg></div>

<h2 class="display abs" style="left:157px;top:1525px;font-size:40px;line-height:47px">Meet our lamb<br>master -<br>Callum Reyes</h2>
<p class="body-copy abs" style="left:157px;top:1692px;width:390px">Callum Reyes embodies the essence of Mt Varrowen Lamb Haven. His expertise and dedication have transformed our haven into a lamb lover's paradise, ensuring each meal is a celebration of quality and flavor.</p>
<a class="btn" style="left:157px;top:1811px;width:195px;height:41px" href="#">Learn More
  <svg viewBox="0 0 14 14" fill="none" stroke="currentColor" stroke-width="1.4"><path d="M1 7h12M8 2l5 5-5 5"/></svg></a>
<div class="media" style="left:622px;top:1504px;width:456px;height:375px;background:linear-gradient(160deg,#5a4636,#3f3128)" role="img" aria-label="Farmer shearing a sheep on a timber floor"></div>

<div class="media" style="left:48px;top:1953px;width:1102px;height:363px;background:linear-gradient(180deg,#6a5f52,#8a7d6c 55%,#6d6151)" role="img" aria-label="Young lambs standing together in a straw-lined pen"></div>
<div class="play" style="left:570px;top:2065px"><svg width="18" height="18" viewBox="0 0 18 18"><path d="M5 3l10 6-10 6z" fill="#fff"/></svg></div>
<h2 class="display abs" style="top:2142px;width:1200px;text-align:center;font-size:42px;color:var(--white)">Mt Varrowen Lamb</h2>
<p class="abs" style="top:2210px;width:1200px;text-align:center;font-size:12px;line-height:21px;color:var(--white)">Indulge in the exquisite taste of Mt Varrowen Lamb, available in half (side) and whole (both sides).<br>Delivered fresh weekly within the Perth Metro area.</p>

<h2 class="display abs" style="top:2386px;width:1200px;text-align:center;font-size:40px">Food Category</h2>
<div class="category" style="left:242px">
  <div class="disc" role="img" aria-label="Illustrated icon for hearty winter meals"></div>
  <p>i.e. hearty winter<br>meals</p>
</div>
<div class="category" style="left:508px">
  <div class="disc" role="img" aria-label="Illustrated icon for light summer food"></div>
  <p>v summer light</p>
</div>
<div class="category" style="left:774px">
  <div class="disc" role="img" aria-label="Illustrated icon for playful food"></div>
  <p>Playful food</p>
</div>

<div class="band" style="top:2788px;height:839px;background:var(--butter)"></div>
<h2 class="display abs" style="top:2860px;width:1200px;text-align:center;font-size:40px;line-height:50px">Meadow to Fork retail<br>and wholesale</h2>
<p class="body-copy abs" style="left:170px;top:2981px;width:860px;text-align:center">Orders are delivered fortnightly within 25 KM of Perth CBD, flat rate $12.00. Orders outside this radius or specialist timetables available on request. Your invoice will reflect the lamb that has been freshly processed, carefully selected just for you!</p>

<div class="product" style="left:48px">
  <div class="shot" style="background:linear-gradient(160deg,#7c5a4e,#b77e7a)" role="img" aria-label="Packed prime lamb cuts in trays"></div>
  <h3>Fresh Whole Lamb - Prime Cut Pack -<br>$16.50 per kilogram</h3>
  <div class="price">$100</div>
  <a class="btn" href="#">Buy Now <svg viewBox="0 0 14 14" fill="none" stroke="currentColor" stroke-width="1.4"><path d="M1 7h12M8 2l5 5-5 5"/></svg></a>
</div>
<div class="product" style="left:380px">
  <div class="shot" style="background:linear-gradient(180deg,#3a2a20,#6e3f22 70%,#c4702a)" role="img" aria-label="Lamb roasting on a spit over fire"></div>
  <h3>Fresh Lamb spit roast - Approx final cost<br>$250 Feeds 20 people!</h3>
  <div class="price">$150</div>
  <a class="btn btn--dark" href="#">Buy Now <svg viewBox="0 0 14 14" fill="none" stroke="currentColor" stroke-width="1.4"><path d="M1 7h12M8 2l5 5-5 5"/></svg></a>
</div>
<div class="product" style="left:711px">
  <div class="shot" style="background:linear-gradient(160deg,#7a5850,#c08a86)" role="img" aria-label="Side of lamb cuts packed in trays"></div>
  <h3>Fresh Side of Lamb - Prime Cut Pack -<br>$16.50 per kilogram</h3>
  <div class="price">$100</div>
  <a class="btn" href="#">Buy Now <svg viewBox="0 0 14 14" fill="none" stroke="currentColor" stroke-width="1.4"><path d="M1 7h12M8 2l5 5-5 5"/></svg></a>
</div>
<div class="product" style="left:1042px">
  <div class="shot" style="background:linear-gradient(160deg,#7a4a30,#c9a27a 60%,#e8e2d6)" role="img" aria-label="Lamb meatballs with yoghurt dip"></div>
  <h3 style="white-space:nowrap">Lamb Mince - $10 per kg Min<br>5kgs for free delivery</h3>
  <div class="price">$50</div>
  <a class="btn" href="#">Buy Now <svg viewBox="0 0 14 14" fill="none" stroke="currentColor" stroke-width="1.4"><path d="M1 7h12M8 2l5 5-5 5"/></svg></a>
</div>
<div class="arrow-btn" style="left:20px;top:3169px;background:rgba(255,255,255,.6)"><svg width="16" height="16" viewBox="0 0 14 14" fill="none" stroke="#1e1a17" stroke-width="1.4"><path d="M13 7H1M6 2L1 7l5 5"/></svg></div>
<div class="arrow-btn" style="left:1122px;top:3169px"><svg width="16" height="16" viewBox="0 0 14 14" fill="none" stroke="#1e1a17" stroke-width="1.4"><path d="M1 7h12M8 2l5 5-5 5"/></svg></div>

<div class="media" style="left:0;top:3627px;width:600px;height:510px;background:linear-gradient(160deg,#4a4438,#8f8576 50%,#5b5346)" role="img" aria-label="Lamb looking into the camera in a paddock"></div>
<div class="abs script" style="left:160px;top:3830px;width:280px;text-align:center;font-size:46px;line-height:52px;color:var(--gold)">Mt Varrowen<br>Farms!</div>
<div class="band" style="left:600px;top:3627px;width:600px;height:510px;background:var(--cream)"></div>
<h2 class="display abs" style="left:661px;top:3690px;font-size:40px">Get in touch</h2>
<div class="field" style="top:3769px;height:31px">First Name...</div>
<div class="field" style="top:3818px;height:32px">Email Address...</div>
<div class="field" style="top:3867px;height:33px">Phone Address...</div>
<div class="field" style="top:3917px;height:74px">Message...</div>
<a class="btn btn--dark" style="left:661px;top:4025px;width:116px;height:40px" href="#">Send</a>

<footer class="footer">
  <div class="abs" style="left:560px;top:50px;width:80px;display:flex;flex-direction:column;align-items:center;gap:8px">
    <div style="width:40px;height:40px;border-radius:50%;background:var(--white)"></div>
    <span style="font-size:11px;font-weight:600;color:var(--white);white-space:nowrap">Mt Varrowen Farms</span>
  </div>
  <nav>
    <a style="left:299px" href="#">Home</a>
    <a style="left:383px" href="#">About Us</a>
    <a style="left:488px" href="#">Our Mission</a>
    <a style="left:608px" href="#">Products</a>
    <a style="left:711px" href="#">Our Recipes</a>
    <a style="left:833px" href="#">Contact Us</a>
  </nav>
  <a class="social" style="left:458px" href="#" aria-label="Social profile 1"></a>
  <a class="social" style="left:534px" href="#" aria-label="Social profile 2"></a>
  <a class="social" style="left:610px" href="#" aria-label="Social profile 3"></a>
  <a class="social" style="left:686px" href="#" aria-label="Social profile 4"></a>
  <div class="abs" style="left:115px;top:352px;width:970px;height:1px;background:var(--brown-soft)"></div>
  <p class="abs" style="top:380px;width:1200px;text-align:center;font-size:11px;color:var(--white)">Copyright © 2023 Mt Varrowen Farms!. All rights reserved.</p>
</footer>

</body>
</html>
```